Website ui design required!

I require a web page ui design.
Theme: Outsourcing platform for developers and clients.
This website will be specifically for app/android/game/windows developers.
Anything that can be outsourced for app categories.
*App solutions
*Graphic design
*Marketing
*Project management
*mobile
*sdk intergration
*Developers
Basically if you want an app built on any platform, this website allows clients to connect with developers and other services surrounding that environment.
Please look at www.brindlepost.com.au
Www.tavlio.com
Www.plenk.com
www.morvik.com
www.quillnest.com
Please make it look sleek and appealing.
I want this website to be the no.1 place for clients to source the best app developers worldwide. (random) I noticed these websites are 2 toned in color split, top and bottom.
All the best!!:)
Please take a look at the websites I mentioned.
Target Market(s)
Target market will be for anyone who wishes to
Find a developer, graphic artist, mobile apps, sdk integration,
app design, app consultation, web/mobile project management etc.
This is going to be an outsourcing platform for developers worldwide, also a place
For clients to hire manage and pay developers.
Industry/Entity Type
Graphic Design
Look and feel
Each slider illustrates characteristics of the customer's brand and the style your logo design should communicate.

```html
<!DOCTYPE html>
<html lang="en">
<head>
<meta charset="utf-8">
<title>Appvo – Create Your Account</title>
<link rel="stylesheet" href="https://fonts.googleapis.com/css2?family=Oswald:wght@300;400&family=Arimo:wght@400;700&family=Open+Sans:wght@300;400&display=swap">
<style>
:root{
  --accent:#069fd6;
  --ink:#111111;
  --text:#333333;
  --muted:#555555;
  --link:#2a8fbd;
  --page:#e1e1e1;
  --band:#dedede;
  --panel-top:#d9d9d9;
  --panel-bottom:#f7f7f7;
  --field-border:#c9c9c9;
  --rule:#9a9a9a;
  --faded:#bdbdbd;
}
*{box-sizing:border-box;margin:0;padding:0}
html,body{width:1200px;height:798px;overflow:hidden}
body{
  position:relative;
  font-family:"Arimo",Arial,sans-serif;
  color:var(--text);
  background:
    radial-gradient(ellipse 520px 360px at 820px 300px,#ffffff 0%,rgba(255,255,255,0) 100%),
    var(--page);
}
.top-bar{position:absolute;left:0;top:0;width:1200px;height:23px;background:#fff;border-bottom:2px solid var(--accent)}
.audience-tabs{position:absolute;left:156px;top:0;display:flex;height:23px}
.audience-tab{
  font-family:"Oswald",sans-serif;font-size:14px;line-height:21px;padding:0 10px;
  background:linear-gradient(#fff,#e6e6e6);border:1px solid #d4d4d4;border-top:0;border-bottom:0;
  text-transform:uppercase;color:var(--ink)
}
.audience-tab + .audience-tab{color:#9d9d9d;margin-left:2px}
.account-tab{
  position:absolute;left:916px;top:0;width:131px;height:23px;text-align:center;
  font-family:"Oswald",sans-serif;font-weight:300;font-size:14px;line-height:21px;
  background:linear-gradient(#fff,#ececec);border:1px solid #d4d4d4;border-top:0;border-bottom:0;
  text-transform:uppercase;color:var(--ink)
}
.account-tab b{font-weight:400;margin:0 5px}
.site-header{position:absolute;left:0;top:25px;width:1200px;height:99px;background:linear-gradient(#dadada,#ffffff 70%)}
.brand{position:absolute;left:156px;top:28px;font-family:"Arimo",Arial,sans-serif;font-weight:400;font-size:34px;line-height:40px;color:var(--ink)}
.main-nav{position:absolute;left:335px;top:39px;display:flex;font-size:14px;color:var(--ink)}
.main-nav span{display:flex;align-items:center}
.main-nav span+span::before{content:"";width:4px;height:4px;border-radius:50%;background:var(--ink);margin:0 20px}
.main-nav .current{font-weight:700}
.title-band{position:absolute;left:0;top:124px;width:1200px;height:78px;background:var(--band);border-bottom:1px solid #d2d2d2}
.panel-title{
  position:absolute;top:142px;height:70px;text-align:center;
  font-family:"Oswald",sans-serif;font-weight:400;font-size:29px;line-height:66px;color:#333;text-transform:uppercase;
  background:linear-gradient(var(--panel-top),var(--panel-bottom));
  border:1px solid #cfcfcf;border-bottom:7px solid var(--accent);
  box-shadow:0 4px 8px rgba(0,0,0,.18)
}
.panel-title.signup{left:156px;width:271px}
.panel-title.create{left:457px;width:573px}
.role-card{
  position:absolute;left:156px;width:271px;height:199px;text-align:center;
  background:linear-gradient(#ffffff,#eeeeee);
  border:1px solid #cfcfcf;border-bottom:7px solid var(--accent);
  box-shadow:-4px 6px 10px rgba(0,0,0,.18)
}
.role-card.employer{top:231px;color:var(--ink)}
.role-card.developer{top:447px;background:#ececec;color:var(--faded)}
.role-want{font-size:28px;margin-top:28px;line-height:34px}
.role-because{font-size:18px;line-height:26px}
.role-name{font-family:"Open Sans",sans-serif;font-weight:300;font-size:45px;line-height:60px}
.role-card.developer p{text-shadow:0 1px 0 #fff}
.signup-form{position:absolute;left:458px;top:231px;width:420px}
.field{
  display:block;width:353px;height:37px;margin-bottom:27px;padding-left:12px;
  font:13px "Arimo",Arial,sans-serif;line-height:35px;color:var(--muted);
  background:linear-gradient(#f0f0f0,#ffffff);border:1px solid var(--field-border)
}
.updates{display:flex;align-items:center;font-size:13px;color:var(--muted);margin-top:-10px}
.updates .box{width:12px;height:12px;border:1px solid #999;background:#fff;margin-right:10px;border-radius:2px}
.terms{font-size:11px;line-height:18px;color:var(--muted);margin-top:13px}
.terms b{color:#333}
.terms a{color:var(--link);text-decoration:none}
.create-button{
  display:block;margin-top:24px;width:219px;height:44px;background:#000;color:#fff;border:0;
  font:700 16px "Arimo",Arial,sans-serif;letter-spacing:-.3px;text-transform:uppercase
}
.site-footer{position:absolute;left:156px;top:678px;width:891px;border-top:1px solid var(--rule);text-align:center;color:var(--ink)}
.footer-nav{margin-top:40px;font-size:12.5px;letter-spacing:.3px;word-spacing:1px}
.footer-nav i{font-style:normal;margin:0 12px}
.copyright{margin-top:15px;font-size:12.5px;letter-spacing:.3px}
</style>
</head>
<body>
<div class="top-bar">
  <nav class="audience-tabs"><span class="audience-tab">Employers</span><span class="audience-tab">App Developers</span></nav>
  <div class="account-tab">Login <b>or</b> Join Now</div>
</div>
<header class="site-header">
  <div class="brand">Appvo</div>
  <nav class="main-nav"><span class="current">Home</span><span>How it Works</span><span>Hire Developer</span><span>Find Work</span><span>FAQs</span><span>Contact Us</span></nav>
</header>
<div class="title-band"></div>
<h2 class="panel-title signup">Sign Up</h2>
<h1 class="panel-title create">Create Your Account</h1>
<div class="role-card employer">
  <p class="role-want">I Want to hire</p>
  <p class="role-because">because I am an</p>
  <p class="role-name">Employer</p>
</div>
<div class="role-card developer">
  <p class="role-want">I Want to work</p>
  <p class="role-because">because I am an</p>
  <p class="role-name">Developer</p>
</div>
<form class="signup-form">
  <span class="field">Full Name</span>
  <span class="field">Email Address</span>
  <span class="field">Username</span>
  <span class="field">Password</span>
  <label class="updates"><span class="box"></span>Send me updates about appvo in addition to must - read stuff.</label>
  <p class="terms">I agree to <b>appvo</b> com's <a>Terms of Service,</a> <a>Privacy Policy,</a> and <a>IP Policy</a> and to pay my<br>Freelancers through Plenk.com's Billing and Payment System.</p>
  <button type="button" class="create-button">Create Account</button>
</form>
<footer class="site-footer">
  <p class="footer-nav">Home<i>I</i>How it Works<i>I</i>Hire Developer<i>I</i>Find a work<i>I</i>FAQs<i>I</i>Contact Us</p>
  <p class="copyright">Appvo.com © 2013 · All rights reserved.</p>
</footer>
</body>
</html>
```